We need a business card design for our website qvwtrading.net. The Star Headline is qvwtrading.net, in large lettering.We sell fashion rings of titanium, mirror pollished stainless steel, and related jewelry. Basically quality products competing with the high expense of gold.We have to portray honesty and trust, because thats who I am. I know marketing, but I am weak on colors and layout. 3D Gold curved edge letters are ok. No green and yellow.Black,Red,Purple and White in small amounts.No fancy Lettering.
No Rainbows in printing.
Our goal is selling our products online globally

Kind Regards Maren Tulloch

Fashion

qvwtrading.net
crafted for comfort every day
email.marentullochptyltd@corvexmail com

```html
<!DOCTYPE html>
<html lang="en">
<head>
<meta charset="utf-8">
<title>qvwtrading.net business card</title>
<link rel="stylesheet" href="https://fonts.googleapis.com/css2?family=Cinzel:wght@400&family=Questrial&display=swap">
<style>
  :root {
    --card-black: #000000;
    --wave-violet: #1c1a33;
    --band-purple: #4f3592;
    --band-edge: #5a3fa6;
    --text-white: #ffffff;
  }
  * { margin: 0; padding: 0; box-sizing: border-box; }
  html, body {
    width: 1200px;
    height: 741px;
    overflow: hidden;
    background: var(--card-black);
  }
  .card {
    position: relative;
    width: 1200px;
    height: 741px;
    background: var(--card-black);
    overflow: hidden;
  }
  .card__backdrop {
    position: absolute;
    inset: 0;
    background:
      radial-gradient(ellipse at 30% 20%, rgba(40, 36, 72, 0.55), transparent 60%),
      radial-gradient(ellipse at 80% 85%, rgba(40, 36, 72, 0.5), transparent 60%),
      var(--card-black);
  }
  .card__site {
    position: absolute;
    top: 236px;
    left: 0;
    width: 1190px;
    text-align: center;
    font-family: "Cinzel", serif;
    font-weight: 400;
    font-size: 84px;
    letter-spacing: 2px;
    line-height: 1;
    color: var(--text-white);
    white-space: nowrap;
  }
  .card__band {
    position: absolute;
    top: 332px;
    left: 0;
    width: 100%;
    height: 67px;
    background: linear-gradient(to right, var(--band-purple) 98.8%, var(--band-edge) 98.8%);
  }
  .card__tagline {
    position: absolute;
    top: 343px;
    left: 0;
    width: 1183px;
    text-align: center;
    font-family: "Questrial", sans-serif;
    font-size: 44px;
    letter-spacing: 2px;
    line-height: 1.2;
    color: var(--text-white);
    white-space: nowrap;
  }
  .card__email {
    position: absolute;
    top: 593px;
    left: 0;
    width: 1183px;
    text-align: center;
    font-family: "Questrial", sans-serif;
    font-size: 42px;
    letter-spacing: 1.5px;
    line-height: 1.2;
    color: var(--text-white);
    white-space: nowrap;
  }
</style>
</head>
<body>
  <main class="card">
    <div class="card__backdrop" role="img" aria-label="Dark background with flowing violet wave lines"></div>
    <h1 class="card__site">QVWTRADING.NET</h1>
    <div class="card__band"></div>
    <p class="card__tagline">crafted for comfort every day</p>
    <p class="card__email">marentullochptyltd@corvexmail.com</p>
  </main>
</body>
</html>
```